Fleeing Marisol Bay website

A very basic website using the graphics provided. The site would give the user the ability to read a description of the book, read testimonials, About the author, Read chapter 1, link to vantoro, order direct via quidlet.

```html
<!DOCTYPE html>
<html lang="en">
<head>
<meta charset="utf-8">
<title>Fleeing Marisol Bay</title>
<link href="https://fonts.googleapis.com/css2?family=Open+Sans:wght@400;600&family=Titillium+Web:wght@400;600&family=Gabriela&display=swap" rel="stylesheet">
<style>
:root{
  --dark:#2f2f2f;
  --orange:#e8900f;
  --orange-light:#f6b21a;
  --text:#2a2a2a;
  --line:#dfe3e7;
  --pay-blue:#2a78c8;
}
*{margin:0;padding:0;box-sizing:border-box}
html,body{width:827px;height:1200px;overflow:hidden}
body{position:relative;background:#fff;font-family:"Open Sans",Arial,sans-serif;color:var(--text)}

/* header */
.site-header{position:absolute;left:0;top:0;width:827px;height:82px;background:linear-gradient(#505050,#2d2d2d)}
.brand{position:absolute;left:124px;top:20px;font-family:"Titillium Web",sans-serif;font-size:18px;line-height:19px;color:var(--orange-light);text-transform:uppercase;letter-spacing:.2px}
.search{position:absolute;left:482px;top:27px;width:132px;height:20px;background:#fff;border-radius:3px;border:1px solid #ccc;font-size:8px;font-style:italic;color:#999;padding:4px 7px}
.search svg{position:absolute;right:6px;top:4px}
.social-top{position:absolute;left:628px;top:28px;display:flex;gap:4px}
.social-top span{font-size:5px;color:#333;background:#e8e8e8;border-radius:50%;width:18px;height:18px;display:flex;align-items:center;justify-content:center;overflow:hidden}

/* nav */
.main-nav{position:absolute;left:0;top:82px;width:827px;height:37px;background:linear-gradient(#f7b416,#e58a0a)}
.main-nav ul{list-style:none;display:flex;position:absolute;left:123px;top:9px}
.main-nav li{font-family:"Titillium Web",sans-serif;font-size:10.5px;color:#fff;padding:3px 10px;margin-right:5px;text-transform:uppercase}
.main-nav li.active{background:#333;border-radius:4px}

/* hero */
.hero{position:absolute;left:0;top:119px;width:827px;height:345px;background:radial-gradient(ellipse at 55% 45%,#fbfbfb 0%,#e9e9e9 60%,#d4d4d4 100%)}
.book{position:absolute;left:153px;top:29px;width:187px;height:280px}
.book-cover{position:absolute;left:0;top:0;width:172px;height:280px;background:linear-gradient(#2a1a16,#5a4536 45%,#2b2520);box-shadow:4px 4px 10px rgba(0,0,0,.35)}
.book-pages{position:absolute;left:172px;top:6px;width:10px;height:268px;background:linear-gradient(90deg,#e8e2cf,#fff)}
.book-title{position:absolute;left:0;width:172px;text-align:center;font-family:"Gabriela",serif;text-transform:uppercase}
.cover-art{position:absolute;left:0;top:66px;width:172px;height:160px;background:linear-gradient(#5d7fa0,#3b5b54 55%,#241d18)}
.hero-copy{position:absolute;left:320px;top:84px;width:400px;text-align:center}
.hero-copy h1{font-family:"Gabriela",serif;font-weight:400;font-size:18.5px;line-height:34px;color:#222;white-space:nowrap}
.hero-copy p{font-family:"Gabriela",serif;font-size:14px;color:var(--orange);margin-top:6px}
.btn-buy{position:absolute;left:457px;top:204px;width:112px;height:40px;background:linear-gradient(#555,#2c2c2c);border-radius:4px;color:#fff;font-weight:600;font-size:16px;display:flex;align-items:center;justify-content:center;letter-spacing:.3px}
.slider-ctrl{position:absolute;left:601px;top:293px;width:107px;height:18px;background:#f4f4f4;border:1px solid #c9c9c9;border-radius:3px;display:flex;align-items:center}
.slider-ctrl .arrows{width:32px;border-right:1px solid #ccc;height:100%;display:flex;align-items:center;justify-content:center}
.dots{display:flex;gap:5px;margin-left:8px}
.dots i{width:5px;height:5px;border-radius:50%;background:#aaa;display:block}
.dots i.on{background:#222}

/* about */
.about{position:absolute;left:0;top:464px;width:827px;height:183px;background:linear-gradient(#f8fafc,#eceff3)}
.author-photo{position:absolute;left:120px;top:24px;width:186px;height:117px;border:3px solid #fff;outline:1px solid #ddd;background:linear-gradient(135deg,#dfe7f0,#9bb4cf 55%,#e9d8c8)}
.section-title{font-size:11px;color:var(--orange);text-transform:uppercase;font-weight:400}
.about .section-title{position:absolute;left:321px;top:27px}
.body-text{font-size:7.3px;line-height:14.2px;color:#333}
.about .body-text{position:absolute;left:321px;top:51px;width:383px;text-align:justify}

/* description */
.desc{position:absolute;left:0;top:647px;width:827px;height:208px;background:#fff}
.desc .desc-title{position:absolute;left:124px;top:28px;font-weight:600;font-size:10px}
.desc .desc-text{position:absolute;left:124px;top:51px;width:345px;text-align:justify}
.ticks{position:absolute;left:124px;top:107px;list-style:none}
.ticks li{font-size:7.8px;color:#333;height:22.4px;display:flex;align-items:center;gap:14px}
.desc .chapter-title{position:absolute;left:479px;top:28px;font-weight:600;font-size:10px}
.chapter-box{position:absolute;left:479px;top:46px;width:225px;height:121px;background:linear-gradient(#fafbfc,#e6e9ec);border:1px solid var(--line);border-radius:5px}
.chapter-box .body-text{position:absolute;left:12px;top:12px;width:200px}
.btn-read{position:absolute;left:161px;top:96px;width:47px;height:17px;background:#111;color:#fff;font-size:7px;display:flex;align-items:center;justify-content:center;border-radius:2px}

/* testimonials */
.testimonials{position:absolute;left:0;top:855px;width:827px;height:229px;background:#f8f9fa;border-top:1px solid #e8e8e8}
.testimonials h2{position:absolute;left:0;width:827px;top:12px;text-align:center;font-family:"Titillium Web",sans-serif;font-weight:400;font-size:15px;color:#444;letter-spacing:.5px}
.quote{position:absolute;top:43px;width:289px;height:92px;background:linear-gradient(#f3f5f7,#dfe4e8);padding:13px 14px;font-size:8.6px;line-height:15px;letter-spacing:.5px;color:#444;text-align:justify}
.quote svg{position:absolute;bottom:-23px;right:0}
.avatar{position:absolute;top:148px;width:52px;height:52px;border-radius:50%;background:linear-gradient(#c9b5a3,#6b5444);border:2px solid #fff}
.person{position:absolute;top:164px;font-size:9.5px;letter-spacing:1px;line-height:15px}
.person b{font-weight:600;color:#333;display:block}
.person span{color:var(--orange)}
.t-dots{position:absolute;top:210px;left:378px;display:flex;gap:5px}
.t-dots i{width:9px;height:9px;border-radius:50%;background:#c8c8c8;display:block}
.t-dots i.on{background:var(--orange)}

/* footer */
.site-footer{position:absolute;left:0;top:1084px;width:827px;height:116px;background:linear-gradient(#454545,#2c2c2c)}
.footer-links{position:absolute;left:0;width:827px;top:22px;text-align:center;font-family:Arial,sans-serif;font-size:7.8px;color:#fff}
.copyright{position:absolute;left:117px;top:67px;font-family:Arial,sans-serif;font-size:7px;color:#eee}
.social-foot{position:absolute;left:335px;top:59px;display:flex;gap:4px}
.social-foot span{width:24px;height:24px;border-radius:50%;background:#eee;color:#333;font-size:5.5px;display:flex;align-items:center;justify-content:center}
.quidlet{position:absolute;left:596px;top:60px;font-weight:600;font-size:15px;color:var(--pay-blue)}
.vantoro{position:absolute;left:672px;top:62px;display:flex;align-items:center;gap:5px}
.vantoro i{display:block;width:12px;height:12px;background:#1f6fb8}
.vantoro span{font-weight:600;font-size:12px;color:#fff}
</style>
</head>
<body>

<header class="site-header">
  <div class="brand">Fleeing<br>Marisol Bay</div>
  <div class="search">Search...
    <svg width="10" height="10" viewBox="0 0 10 10"><circle cx="4" cy="4" r="3" fill="none" stroke="#777" stroke-width="1.4"/><line x1="6.2" y1="6.2" x2="9.3" y2="9.3" stroke="#777" stroke-width="1.6"/></svg>
  </div>
  <div class="social-top"><span>Trillo</span><span>Folkly</span><span>Gleamr</span><span>Linkw.</span></div>
</header>

<nav class="main-nav">
  <ul>
    <li class="active">Home</li><li>Book Info</li><li>Purchase</li><li>About Author</li><li>Quick View</li><li>Contact Us</li>
  </ul>
</nav>

<section class="hero">
  <div class="book">
    <div class="book-pages"></div>
    <div class="book-cover">
      <div class="book-title" style="top:16px;font-size:14px;color:#f4e6b0">Fleeing</div>
      <div class="book-title" style="top:36px;font-size:19px;color:#f2a020">Marisol Bay</div>
      <div class="cover-art" role="img" aria-label="Silhouette of a man behind prison bars with a tropical beach beyond"></div>
      <div class="book-title" style="top:244px;font-size:13px;color:#eee;letter-spacing:.5px">Rowan Castell</div>
    </div>
  </div>
  <div class="hero-copy">
    <h1>Lorem Ipsum is simply dummy text of the<br>printing and typesetting industry</h1>
    <p>Lorem Ipsum is simply dummy text</p>
  </div>
  <div class="btn-buy">BUY NOW</div>
  <div class="slider-ctrl">
    <div class="arrows"><svg width="16" height="8" viewBox="0 0 16 8"><path d="M5 1 2 4 5 7" fill="none" stroke="#222" stroke-width="1.5"/><path d="M11 1 14 4 11 7" fill="none" stroke="#888" stroke-width="1.5"/></svg></div>
    <div class="dots"><i></i><i></i><i class="on"></i><i></i><i></i><i></i></div>
  </div>
</section>

<section class="about">
  <div class="author-photo" role="img" aria-label="Close-up of a hand writing with a pen on paper"></div>
  <h2 class="section-title">About the Author</h2>
  <p class="body-text">At vero eos et accusam et justo duo dolores et ea rebum. Stet clita kasd gubergren, no sea takimata sanctus est Lorem ipsum dolor sit amet. Lorem ipsum dolor sit amet, consetetur sadipscing elitr, sed diam nonumy eirmod tempor invidunt ut labore et dolore magna aliquyam erat, sed diam voluptua. Lorem ipsum dolor sit amet, consetetur sadipscing elitr, sed diam nonumy eirmod tempor invidunt ut labore et dolore magna aliquyam erat, sed diam voluptua. At vero eos et accusam et justo duo dolores et ea rebum. Stet clita kasd gubergren, no sea takimata sanctus est Lorem ipsum dolor sit amet</p>
</section>

<section class="desc">
  <h2 class="section-title desc-title">Description of the Book</h2>
  <p class="body-text desc-text">Lorem ipsum dolor sit amet, consetetur sadipscing elitr, sed diam nonumy eirmod tempor invidunt ut labore et dolore magna aliquyam erat, sed diam voluptua. At vero eos et accusam et justo duo dolores et ea rebum. Stet clita kasd gubergren, no sea takimata sanctus est Lorem ipsum</p>
  <ul class="ticks">
    <li><svg width="11" height="11" viewBox="0 0 11 11"><circle cx="5.5" cy="5.5" r="5.5" fill="#f08a24"/><path d="M3 5.6 4.8 7.4 8.2 3.8" fill="none" stroke="#fff" stroke-width="1.5"/></svg>Lorem ipsum dolor sit amet, consetetur sadipscing elitr.</li>
    <li><svg width="11" height="11" viewBox="0 0 11 11"><circle cx="5.5" cy="5.5" r="5.5" fill="#f08a24"/><path d="M3 5.6 4.8 7.4 8.2 3.8" fill="none" stroke="#fff" stroke-width="1.5"/></svg>At vero eos et accusam et justo duo dolores et ea rebum.</li>
    <li><svg width="11" height="11" viewBox="0 0 11 11"><circle cx="5.5" cy="5.5" r="5.5" fill="#f08a24"/><path d="M3 5.6 4.8 7.4 8.2 3.8" fill="none" stroke="#fff" stroke-width="1.5"/></svg>Ut labore et dolore magna aliquyam erat, sed diam voluptua.</li>
  </ul>
  <h2 class="section-title chapter-title">Chapter 1</h2>
  <div class="chapter-box">
    <p class="body-text">Lorem ipsum dolor sit amet, consetetur sadipscing elitr, sed diam nonumy eirmod tempor invidunt ut labore et dolore magna aliquyam erat, Lorem ipsum dolor sit amet, consetetur sadipscing elitr, sed diam nonumy eirmod tempor invidunt ut labore et dolore magna aliquyam erat,</p>
    <div class="btn-read">READ</div>
  </div>
</section>

<section class="testimonials">
  <h2>TESTIMONIAL</h2>
  <blockquote class="quote" style="left:120px">“Lorem ipsum dolor sit amet, consectetur adipiscing elit. Donec tempor nibh eget orci tincidunt placerat. Sed viverra risus nec gravida dapibus. In fringilla vestibulum turpis quis condimentum. Aliquam erat volutpat”
    <svg width="60" height="23" viewBox="0 0 60 23"><path d="M20 0H60L0 23Z" fill="#dfe4e8"/></svg></blockquote>
  <blockquote class="quote" style="left:424px">“Lorem ipsum dolor sit amet, consectetur adipiscing elit. Donec tempor nibh eget orci tincidunt placerat. Sed viverra risus nec gravida dapibus. In fringilla vestibulum turpis quis condimentum. Aliquam erat volutpat”
    <svg width="60" height="23" viewBox="0 0 60 23"><path d="M20 0H60L0 23Z" fill="#dfe4e8"/></svg></blockquote>
  <div class="avatar" role="img" aria-label="Portrait of reviewer" style="left:179px"></div>
  <div class="person" style="left:248px"><b>Dorian Vale</b><span>Lorem ipsum</span></div>
  <div class="avatar" role="img" aria-label="Portrait of reviewer" style="left:492px;top:146px"></div>
  <div class="person" style="left:562px;top:162px"><b>Dorian Vale</b><span>Lorem ipsum</span></div>
  <div class="t-dots"><i></i><i class="on"></i><i></i><i></i><i></i><i></i></div>
</section>

<footer class="site-footer">
  <div class="footer-links">Terms of Service | Returns | Policy Privacy | Event | Contact | Blog | Sitemap</div>
  <div class="copyright">Copy Right © 2014. All rights reserved.</div>
  <div class="social-foot"><span>Trillo</span><span>Folkly</span><span>Gleamr</span><span>Linkw.</span><span>Vidora</span></div>
  <div class="quidlet">quidlet</div>
  <div class="vantoro"><i></i><span>vantoro</span></div>
</footer>

</body>
</html>
```